Web Design Project

We are an IT System Integrator. We provide Norvik 500 ERP System, CRM etc. We also provide hardware, networking servicing. Please look at www.brinquot.com.sg. They provide the same service as us. We like to redesign our web site. I will attached the color that I prefer for reference.

Our website is www.ravdu.com.sg.  It has been created about 14 years ago.  We are trying to revamp it with a new look and information.   The new website must be informative, fast.    I have attached an attachment which show the color that I prefer(brownish golden).   

Our competitor (www.brinquot.com) is carrying the same trade as us.  They have all the informations In their website that we will like to have.  Therefore I recommend you to take a look at my competitor website and have a better   
understanding on the kind of information I would like to have for my new website.

This project is guarantee to the person with the best design.  We can have it guarantee.

Target Market(s)

Corporate and companies

Industry/Entity Type

Hardware

```html
<!DOCTYPE html>
<html lang="en">
<head>
<meta charset="utf-8">
<title>Ravdu Information System</title>
<link href="https://fonts.googleapis.com/css2?family=Open+Sans:wght@400;600;700;800&display=swap" rel="stylesheet">
<style>
:root{
  --gold:#b08d45;
  --gold-dark:#8b6421;
  --gold-text:#9a6f2a;
  --ink:#111111;
  --body:#666666;
  --orange:#e0400e;
  --link:#c8501a;
  --white:#ffffff;
  --header-bg:#fafafa;
}
*{box-sizing:border-box;margin:0;padding:0}
html,body{width:1200px;height:600px;overflow:hidden;background:var(--white);font-family:"Open Sans",Arial,sans-serif}
.page{position:relative;width:1200px;height:600px;overflow:hidden}

.top-bar{position:absolute;left:0;top:0;width:1200px;height:22px;background:var(--gold);color:var(--white);font-size:11px}
.top-bar .contact{position:absolute;left:209px;top:3px;display:flex;align-items:center;gap:5px}
.top-bar .contact svg{display:block}
.top-bar .contact .gap{width:4px}
.top-bar .follow{position:absolute;left:679px;top:3px;display:flex;align-items:center;gap:6px}
.social-dot{width:11px;height:11px;border-radius:50%;background:var(--white)}

.site-header{position:absolute;left:0;top:22px;width:1200px;height:76px;background:var(--header-bg)}
.brand{position:absolute;left:208px;top:18px;display:flex;align-items:center;gap:7px}
.brand-mark{width:30px;height:30px;border-radius:50%;background:var(--gold-dark)}
.brand-name{font-size:12px;font-weight:700;color:var(--gold-dark);line-height:1.2;width:100px}
.main-nav{position:absolute;top:29px;left:417px;display:flex;font-size:14.5px;font-weight:700;letter-spacing:.4px;color:var(--ink)}
.main-nav span{margin-right:17px}
.main-nav .plus{color:var(--gold);font-weight:600;margin:0 0 0 2px}
.main-nav .active{color:var(--gold-text)}

.hero{position:absolute;left:0;top:98px;width:1200px;height:323px;
  background:
   linear-gradient(90deg,rgba(40,60,120,.55) 0%,rgba(0,0,0,0) 30%,rgba(0,0,0,0) 70%,rgba(40,60,120,.5) 100%),
   linear-gradient(180deg,#b9bcc4 0%,#9fa4ad 25%,#b33a3a 55%,#d8d8da 80%,#a9a7a4 100%)}
.hero-title{position:absolute;left:539px;top:15px;width:389px;height:72px;background:var(--ink);color:var(--white);font-size:46px;font-weight:700;text-align:right;padding-right:40px;line-height:72px;letter-spacing:.5px}
.hero-sub{position:absolute;left:610px;top:102px;width:309px;height:45px;background:var(--orange);color:var(--white);font-size:37px;font-weight:700;text-align:right;padding-right:25px;line-height:45px;letter-spacing:.5px}
.slide-arrow{position:absolute;top:128px;width:32px;height:32px;background:var(--white);display:flex;align-items:center;justify-content:center}
.slide-arrow.prev{left:19px}
.slide-arrow.next{left:1148px}
.slide-dots{position:absolute;top:300px;left:593px;display:flex;gap:5px}
.slide-dots span{width:20px;height:20px;border-radius:50%;background:var(--ink);border:2px solid var(--white)}
.slide-dots .current{background:#c06a0a}

.features{position:absolute;top:461px;left:0;width:1200px}
.feature{position:absolute;width:171px}
.feature-head{display:flex;align-items:center;gap:4px;margin-left:18px;height:36px}
.feature-icon{flex:none;width:35px;height:35px;border-radius:50%;background:var(--gold-dark);display:flex;align-items:center;justify-content:center}
.feature-title{font-size:16px;font-weight:600;color:var(--ink);line-height:16px;letter-spacing:.3px}
.feature-text{margin-top:8px;font-size:10.5px;line-height:13.4px;color:var(--body);letter-spacing:.2px}
.read-more{display:block;text-align:right;margin-top:5px;font-size:11.5px;color:var(--link);letter-spacing:.2px}
</style>
</head>
<body>
<div class="page">
  <div class="top-bar">
    <div class="contact">
      <svg width="12" height="14" viewBox="0 0 12 14"><path d="M2 1 L5 1 L6 4 L4 5.5 Q5.5 9 8 10 L9.5 8.5 L12 10 L11 13 Q4 13 1 4 Z" fill="#fff"/></svg>
      <span>Call Us : +8(800)555-0142</span>
      <span class="gap"></span>
      <svg width="16" height="12" viewBox="0 0 16 12"><rect x=".5" y=".5" width="15" height="11" fill="none" stroke="#fff"/><path d="M.5 .5 L8 7 L15.5 .5" fill="none" stroke="#fff"/></svg>
      <span>info@ravduinfosystem.com</span>
    </div>
    <div class="follow">
      <span>Follow Us:</span>
      <span class="social-dot"></span>
      <span class="social-dot"></span>
      <span class="social-dot"></span>
    </div>
  </div>

  <header class="site-header">
    <div class="brand">
      <span class="brand-mark"></span>
      <span class="brand-name">Ravdu Information System</span>
    </div>
    <nav class="main-nav">
      <span class="active">HOME<span class="plus"> +</span></span>
      <span>COMPANY<span class="plus">+</span></span>
      <span>PRODUCT<span class="plus"> +</span></span>
      <span>SERVICES<span class="plus"> +</span></span>
      <span>INFOBIN<span class="plus">+</span></span>
      <span>CONTACT<span class="plus">+</span></span>
    </nav>
  </header>

  <section class="hero" role="img" aria-label="Photo of a busy warehouse aisle with stocked shelving and a moving forklift">
    <div class="hero-title">WAREHOUSE</div>
    <div class="hero-sub">MANAGEMENT</div>
    <div class="slide-arrow prev"><svg width="16" height="14" viewBox="0 0 16 14"><path d="M8 1 L2 7 L8 13 M14 1 L8 7 L14 13" fill="none" stroke="#111" stroke-width="2.4"/></svg></div>
    <div class="slide-arrow next"><svg width="16" height="14" viewBox="0 0 16 14"><path d="M2 1 L8 7 L2 13 M8 1 L14 7 L8 13" fill="none" stroke="#111" stroke-width="2.4"/></svg></div>
    <div class="slide-dots"><span class="current"></span><span></span><span></span></div>
  </section>

  <section class="features">
    <article class="feature" style="left:211px">
      <div class="feature-head">
        <span class="feature-icon"><svg width="20" height="20" viewBox="0 0 20 20"><path d="M3 3 L6 3 L9 14 L16 14" fill="none" stroke="#fff" stroke-width="1.6"/><rect x="8" y="6" width="7" height="6" fill="#fff"/><circle cx="9" cy="17" r="1.6" fill="#fff"/><circle cx="15" cy="17" r="1.6" fill="#fff"/></svg></span>
        <h2 class="feature-title">Warehouses</h2>
      </div>
      <p class="feature-text">Lorem ipsum dolor sit amet, consectetur adipisicing elit, sed do eiusmod tempor incididunt ut labore et.</p>
      <a class="read-more">Read More</a>
    </article>
    <article class="feature" style="left:411px">
      <div class="feature-head">
        <span class="feature-icon"><svg width="20" height="20" viewBox="0 0 20 20"><rect x="3" y="2" width="14" height="4" rx="1" fill="#fff"/><rect x="3" y="8" width="14" height="4" rx="1" fill="#fff"/><rect x="3" y="14" width="14" height="4" rx="1" fill="#fff"/></svg></span>
        <h2 class="feature-title">Servers</h2>
      </div>
      <p class="feature-text">Lorem ipsum dolor sit amet, consectetur adipisicing elit, sed do eiusmod tempor incididunt ut labore et.</p>
      <a class="read-more">Read More</a>
    </article>
    <article class="feature" style="left:610px">
      <div class="feature-head">
        <span class="feature-icon"><svg width="20" height="20" viewBox="0 0 20 20"><rect x="5" y="2" width="10" height="5" fill="#fff"/><rect x="2" y="8" width="16" height="7" rx="1" fill="#fff"/><rect x="5" y="13" width="10" height="5" fill="#fff" stroke="#8b6421"/></svg></span>
        <h2 class="feature-title">Printers</h2>
      </div>
      <p class="feature-text">Lorem ipsum dolor sit amet, consectetur adipisicing elit, sed do eiusmod tempor incididunt ut labore et.</p>
      <a class="read-more">Read More</a>
    </article>
    <article class="feature" style="left:812px">
      <div class="feature-head">
        <span class="feature-icon"><svg width="20" height="20" viewBox="0 0 20 20"><path d="M3 5 L15 9 L13 14 L2 10 Z" fill="#fff"/><rect x="15" y="9" width="3" height="7" fill="#fff"/></svg></span>
        <h2 class="feature-title">Surveillance Camera</h2>
      </div>
      <p class="feature-text">Lorem ipsum dolor sit amet, consectetur adipisicing elit, sed do eiusmod tempor incididunt ut labore et.</p>
      <a class="read-more">Read More</a>
    </article>
  </section>
</div>
</body>
</html>
```